Lumo Organic Baby Wipes for retail sales into supermarkets

Design a new Organic Baby Wipes Pack that has a similar feel and details to the attachments under the Brand Name LUMO Organics. Please keep all writing in English and highlight the following info on the Pack. - 80 Pack, 100% Biodegradable,
Aloe Vera, Chamomile,Natural Vitamin E to soothe baby's skin.
Hypo Allergenic, pH Balanced for baby's skin.
Fragrance Free, Alcohol Free, Chlorine Free, Parabens Free.

Target Market(s)

Mums looking for a Organic Baby Wipe

Industry/Entity Type

Baby

Font styles to use
Sans Serif

Colors
9bcb3c
abd036
cadf82
ffffff

Requirements
Must have
• Lumo Organics, White Base, majority green writing with different shades, touches of Brown to represent Bamboo Wipes.
• Please make ORGANIC writing very big.
Nice to have
• Natural Organic feel going to use matt packaging.
Should not have
• Cluttered too much information

```html
<!DOCTYPE html>
<html lang="en">
<head>
<meta charset="utf-8">
<title>Lumo Organics – Organic Baby Wipes Pack</title>
<link href="https://fonts.googleapis.com/css2?family=Kalam:wght@700&family=Oswald:wght@400&display=swap" rel="stylesheet">
<style>
  :root {
    --green-main: #8cc63f;
    --green-bright: #9bcb3c;
    --green-mid: #abd036;
    --green-pale: #cadf82;
    --green-deep: #3f8f2a;
    --bamboo-brown: #7a5a3a;
    --plum: #3a1a40;
    --white: #ffffff;
    --stage: #e6e6e6;
  }
  * { box-sizing: border-box; margin: 0; padding: 0; }
  html, body { width: 1200px; height: 806px; overflow: hidden; }
  body {
    background: var(--stage);
    position: relative;
    font-family: "Kalam", sans-serif;
  }
  .pack {
    position: absolute;
    left: 50px; top: 43px;
    width: 1100px; height: 720px;
    background: linear-gradient(180deg, #ffffff 0%, #f6f6f6 100%);
    overflow: hidden;
  }
  .brand-tab {
    position: absolute;
    left: 455px; top: 0;
    width: 190px; height: 112px;
    background: var(--white);
    border: 2px solid var(--plum);
    border-top: none;
    border-radius: 0 0 16px 16px;
    display: flex; align-items: center; justify-content: center;
  }
  .brand-name {
    font-family: "Kalam", sans-serif;
    font-weight: 700;
    font-size: 64px;
    color: var(--plum);
    line-height: 1;
    padding-top: 8px;
  }
  .baby-photo {
    position: absolute;
    left: 40px; top: 95px;
    width: 230px; height: 400px;
    border-radius: 110px 110px 40px 40px;
    background: radial-gradient(ellipse at 50% 35%, #f1d6c4 0%, #e8c2a8 45%, #f4ece6 80%, rgba(255,255,255,0) 100%);
  }
  .headline {
    position: absolute;
    left: 270px; top: 170px;
    font-weight: 700;
    font-size: 96px;
    line-height: 1;
    color: var(--green-main);
    transform: rotate(-6deg);
    transform-origin: left center;
    white-space: nowrap;
    letter-spacing: -1px;
  }
  .subhead {
    position: absolute;
    left: 330px; top: 330px;
    width: 420px;
    font-weight: 700;
    font-size: 76px;
    line-height: 1.1;
    color: var(--green-main);
    text-align: center;
    transform: rotate(-4deg);
  }
  .benefit-band {
    position: absolute;
    left: 0; top: 555px;
    width: 440px; height: 58px;
    background: var(--green-main);
    color: var(--white);
    font-family: "Oswald", sans-serif;
    font-variant: small-caps;
    font-size: 15px;
    line-height: 1.5;
    padding: 6px 14px;
  }
  .badge-row {
    position: absolute;
    left: 26px; top: 622px;
    display: flex; gap: 6px;
  }
  .badge { width: 72px; height: 72px; }
  .badge text {
    font-family: "Oswald", sans-serif;
    font-size: 9px;
    fill: var(--green-deep);
    letter-spacing: 0.5px;
  }
  .bamboo-art {
    position: absolute;
    right: 0; top: 0;
    width: 300px; height: 720px;
    background: linear-gradient(90deg, rgba(255,255,255,0) 0%, #cfe6a8 30%, #5aa83a 60%, #2f7d2a 85%, var(--bamboo-brown) 100%);
  }
  .pack-count {
    position: absolute;
    right: -70px; bottom: 60px;
    width: 420px; height: 80px;
    background: var(--green-mid);
    transform: rotate(-42deg);
    display: flex; align-items: center; justify-content: center;
    border-top: 2px dashed var(--white);
    border-bottom: 2px dashed var(--white);
    outline: 6px solid var(--green-mid);
    color: var(--white);
    font-weight: 700;
    font-size: 56px;
    line-height: 1;
  }
</style>
</head>
<body>
  <main class="pack">
    <div class="bamboo-art" role="img" aria-label="Green bamboo stalks and leaves"></div>

    <header class="brand-tab">
      <span class="brand-name">Lumo</span>
    </header>

    <div class="baby-photo" role="img" aria-label="Photo of a crawling baby in a nappy"></div>

    <h1 class="headline">LUMO ORGANIC</h1>
    <h2 class="subhead">Organic Baby Wipes Pack</h2>

    <p class="benefit-band">
      Aloe Vera, Chamomile, Natural Vitamin E to soothe baby's skin.<br>
      Hypo Allergenic, pH Balanced for baby's skin.
    </p>

    <ul class="badge-row" aria-label="Product claims">
      <li style="list-style:none">
        <svg class="badge" viewBox="0 0 72 72" aria-label="100% Biodegradable">
          <defs><path id="arc1" d="M10,36 a26,26 0 0,0 52,0"/></defs>
          <circle cx="36" cy="36" r="33" fill="none" stroke="var(--green-pale)" stroke-width="1.5"/>
          <circle cx="36" cy="30" r="11" fill="var(--green-main)"/>
          <text><textPath href="#arc1" startOffset="50%" text-anchor="middle">100% BIODEGRADABLE</textPath></text>
        </svg>
      </li>
      <li style="list-style:none">
        <svg class="badge" viewBox="0 0 72 72" aria-label="Fragrance Free">
          <defs><path id="arc2" d="M10,36 a26,26 0 0,0 52,0"/></defs>
          <circle cx="36" cy="36" r="33" fill="none" stroke="var(--green-pale)" stroke-width="1.5"/>
          <circle cx="36" cy="30" r="11" fill="var(--green-pale)"/>
          <text><textPath href="#arc2" startOffset="50%" text-anchor="middle">FRAGRANCE FREE</textPath></text>
        </svg>
      </li>
      <li style="list-style:none">
        <svg class="badge" viewBox="0 0 72 72" aria-label="Alcohol Free">
          <defs><path id="arc3" d="M10,36 a26,26 0 0,0 52,0"/></defs>
          <circle cx="36" cy="36" r="33" fill="none" stroke="var(--green-pale)" stroke-width="1.5"/>
          <rect x="32" y="18" width="8" height="24" rx="3" fill="var(--green-main)"/>
          <text><textPath href="#arc3" startOffset="50%" text-anchor="middle">ALCOHOL FREE</textPath></text>
        </svg>
      </li>
      <li style="list-style:none">
        <svg class="badge" viewBox="0 0 72 72" aria-label="Chlorine Free">
          <defs><path id="arc4" d="M10,36 a26,26 0 0,0 52,0"/></defs>
          <circle cx="36" cy="36" r="33" fill="none" stroke="var(--green-pale)" stroke-width="1.5"/>
          <circle cx="36" cy="30" r="9" fill="none" stroke="var(--green-main)" stroke-width="3"/>
          <text><textPath href="#arc4" startOffset="50%" text-anchor="middle">CHLORINE FREE</textPath></text>
        </svg>
      </li>
      <li style="list-style:none">
        <svg class="badge" viewBox="0 0 72 72" aria-label="Parabens Free">
          <defs><path id="arc5" d="M10,36 a26,26 0 0,0 52,0"/></defs>
          <circle cx="36" cy="36" r="33" fill="none" stroke="var(--green-pale)" stroke-width="1.5"/>
          <circle cx="36" cy="30" r="11" fill="var(--green-bright)"/>
          <text><textPath href="#arc5" startOffset="50%" text-anchor="middle">PARABENS FREE</textPath></text>
        </svg>
      </li>
    </ul>

    <div class="pack-count">80 Pack</div>
  </main>
</body>
</html>
```